Baby Boutique Needs a Business Card Design

We need a modern double sided business card design using the attached logo for Lil' Tot Nook.

Lil' Tot Nook is a baby boutique which sells only handmade clothing and accessories for both boys and girls. Our store will live exclusively online.

We would like to only use the colors that have been used in the logo.

Target Market(s)

Potential wholesale clients, Small business owners

Industry/Entity Type

Retail

Contact Information for Business Card

Name Wendell J. Ferris (Owner)
Email sales@ltotnook.com
Main Phone 787-203-6159
Cell phone 787-203-6742
Website www.LTotNook.com

Font styles to use
Sans Serif

Colors

Designer to choose colors to be used in the design.

Requirements
Must have
• -Would like to have icons that indentify the contact information.
• -Include our website
• -Include our tagline in a small area near the bottom. "Handmade Baby Creations"
• -Would like to include Facebook and Instagram Icons
• -
Nice to have
• Would like to have a simple back side with the logo.
• Something along the lines of the harbor ledger card attached.

```html
<!DOCTYPE html>
<html lang="en">
<head>
<meta charset="utf-8">
<title>Lil' Tot Nook — Business Card</title>
<link href="https://fonts.googleapis.com/css2?family=Questrial&display=swap" rel="stylesheet">
<style>
  :root {
    --backdrop: #e4e4e4;
    --card-navy: #1b2434;
    --mint: #5ccfbc;
    --mint-soft: #4fb8a7;
    --card-edge: #f2f2f2;
  }
  * { margin: 0; padding: 0; box-sizing: border-box; }
  html, body {
    width: 1200px;
    height: 900px;
    overflow: hidden;
    background: var(--backdrop);
    font-family: "Questrial", "Century Gothic", sans-serif;
  }
  .canvas {
    width: 1200px;
    height: 900px;
    display: flex;
    flex-direction: column;
    align-items: center;
    justify-content: center;
    gap: 44px;
  }
  .card {
    width: 595px;
    height: 340px;
    background: var(--card-navy);
    position: relative;
    box-shadow: 0 8px 22px rgba(0,0,0,0.18);
  }
  .brand-mark {
    display: flex;
    align-items: center;
    gap: 10px;
    color: var(--mint);
    font-size: 26px;
    line-height: 1;
    white-space: nowrap;
  }
  .brand-dot {
    width: 14px;
    height: 14px;
    border-radius: 50%;
    background: var(--mint);
    flex: none;
  }
  .card--front .brand-mark {
    position: absolute;
    left: 50%;
    top: 50%;
    transform: translate(-50%, -50%);
    font-size: 30px;
  }
  .card--back .brand-mark {
    position: absolute;
    left: 52px;
    top: 50%;
    transform: translateY(-50%);
    font-size: 24px;
  }
  .contact-block {
    position: absolute;
    left: 318px;
    top: 88px;
    color: var(--mint);
  }
  .contact-name {
    font-size: 19px;
    letter-spacing: 1px;
    text-transform: uppercase;
  }
  .contact-role {
    font-size: 14px;
    letter-spacing: 7px;
    margin-top: 2px;
    color: var(--mint-soft);
  }
  .contact-list {
    list-style: none;
    margin-top: 16px;
  }
  .contact-item {
    display: flex;
    align-items: center;
    gap: 14px;
    font-size: 13px;
    height: 22px;
    color: var(--mint-soft);
  }
  .contact-icon {
    width: 14px;
    height: 14px;
    flex: none;
    fill: var(--mint);
  }
</style>
</head>
<body>
<main class="canvas">

  <section class="card card--front" aria-label="Card front">
    <div class="brand-mark"><span class="brand-dot"></span>Lil' Tot Nook</div>
  </section>

  <section class="card card--back" aria-label="Card back">
    <div class="brand-mark"><span class="brand-dot"></span>Lil' Tot Nook</div>

    <div class="contact-block">
      <p class="contact-name">Wendell J. Ferris</p>
      <p class="contact-role">investor</p>
      <ul class="contact-list">
        <li class="contact-item">
          <svg class="contact-icon" viewBox="0 0 16 16" aria-hidden="true"><path d="M1 3h14v10H1z M2 4.2v.3l6 4.3 6-4.3v-.3z" fill-rule="evenodd"/></svg>
          sales@ltotnook.com
        </li>
        <li class="contact-item">
          <svg class="contact-icon" viewBox="0 0 16 16" aria-hidden="true"><path d="M3.5 1.5l2.6 3-1.4 1.6c.9 2 2.3 3.4 4.3 4.3l1.6-1.4 3 2.6-1.6 2.4C7 13.6 2.4 9 1.1 3.1z"/></svg>
          787-203-6159
        </li>
        <li class="contact-item">
          <svg class="contact-icon" viewBox="0 0 16 16" aria-hidden="true"><path d="M1 5c0-2 3-3 7-3s7 1 7 3v1.5h-3.5V5h-7v1.5H1z M3 8h10l1.5 6h-13z"/></svg>
          787-203-6742
        </li>
        <li class="contact-item">
          <svg class="contact-icon" viewBox="0 0 16 16" aria-hidden="true"><circle cx="8" cy="8" r="7"/><path d="M1 8h14 M8 1c-3 3.5-3 10.5 0 14 M8 1c3 3.5 3 10.5 0 14" stroke="#1b2434" stroke-width="1.1" fill="none"/></svg>
          www.LTotNook.com
        </li>
      </ul>
    </div>
  </section>

</main>
</body>
</html>
```